Business Cards for new orthopaedic surgery practice

My husband and I are starting our own orthopaedic surgery practice. We are looking for a business card that is uniform, but one will have my name/title and the other will have his. You can just create one design with my name on it for now. But when I choose your design as the winning design I will ask that you add another copy with his name/title.

We are looking for classy, simple, elite all in one. We like dark blues/a little gold/yellow. Something that goes with our logo. We want our logo incorporated. Here is all the info you need:
Business name: RV Spine & Vitality Center
Location: 38915 North Bramble Ave
Maple Ridge, FL 33482
Phone: 954-218-4630
Fax: 954-571-2846
Email: info@myrvspine.example

Names: Lucinda Ferrow, M.D.
Board Certified Hand and Upper Extremity Surgeon

Emeka Dlunga, M.D.
Board Certified Hip & Knee Replacement/General Orthopaedic Surgeon

Can decide what you want to put on the back. Maybe a slogan:
Steady Hands. Centered on You

I am just going to upload our logo. The only thing is if we select you as the winning design, the location, and phone numbers may change. We will need your help to update that once fully solidified.

Industry/Entity Type

Medical

Contact Information for Business Card

Colors
0054AA
0677BA
7BADD7
CADEEF
E8F1F8
0094D4
00A9DD
6FCCEA
C7EBF8
E9F6FB

Requirements
Must have
• class, appeal,
Should not have
• We want to air on the side of masculine if we are looking at masculine vs. feminine feel. But we still want it classy, sophisticated, and something we will love

```html
<!DOCTYPE html>
<html lang="en">
<head>
<meta charset="utf-8">
<title>RV Spine &amp; Vitality Center — Business Cards</title>
<link href="https://fonts.googleapis.com/css2?family=Poppins:wght@400;500;700&family=Cormorant+Garamond:wght@600&display=swap" rel="stylesheet">
<style>
  :root {
    --stage: #8a8a8a;
    --card: #cfcfd1;
    --card-edge: #e6e6e8;
    --navy: #213f93;
    --gold: #e9c66b;
    --icon-bg: #f3ecd6;
    --spine: rgba(120, 124, 134, 0.28);
  }
  * { box-sizing: border-box; margin: 0; padding: 0; }
  html, body { width: 1200px; height: 800px; overflow: hidden; }
  body {
    background: var(--stage);
    font-family: "Poppins", sans-serif;
    color: var(--navy);
    position: relative;
  }
  .card {
    position: absolute;
    background: linear-gradient(160deg, #dadadc, var(--card));
    border: 2px solid var(--card-edge);
    border-radius: 22px;
    overflow: hidden;
    box-shadow: 0 18px 40px rgba(0,0,0,0.18);
  }

  /* Front: portrait card, content set sideways */
  .card-front { left: 90px; top: 120px; width: 340px; height: 560px; }
  .front-layout {
    position: absolute;
    width: 560px; height: 340px;
    left: -110px; top: 110px;
    transform: rotate(-90deg);
  }
  .front-spine {
    position: absolute; left: 40px; top: 110px; width: 480px; height: 60px;
    border-radius: 30px;
    background: linear-gradient(90deg, transparent, var(--spine) 20%, var(--spine) 80%, transparent);
  }
  .front-brand {
    position: absolute; left: 0; right: 0; top: 92px;
    text-align: center;
    font-family: "Cormorant Garamond", serif;
    font-weight: 600; font-size: 40px; line-height: 1.05;
    color: var(--navy);
  }
  .front-brand .mark {
    display: inline-block; width: 20px; height: 20px; border-radius: 50%;
    background: var(--navy); margin-right: 12px; vertical-align: 4px;
  }
  .slogan-pill {
    position: absolute; left: 70px; right: 70px; bottom: 56px; height: 50px;
    border-radius: 25px; background: var(--navy); color: var(--gold);
    display: flex; align-items: center; justify-content: center;
    font-size: 19px; letter-spacing: 1.5px; white-space: nowrap;
  }

  /* Back: landscape card */
  .card-back { left: 530px; top: 230px; width: 580px; height: 350px; }
  .name-block { position: absolute; left: 0; top: 38px; padding-left: 34px; }
  .name-block::before {
    content: ""; position: absolute; left: 18px; top: 2px; width: 8px; height: 44px;
    background: var(--navy);
  }
  .doctor-name { font-weight: 700; font-size: 26px; letter-spacing: 1px; line-height: 1.1; white-space: nowrap; }
  .doctor-title { font-size: 9px; font-weight: 500; letter-spacing: 0.4px; text-transform: uppercase; margin-top: 3px; }
  .contact-list { position: absolute; left: 0; top: 128px; list-style: none; }
  .contact-item { display: flex; align-items: flex-start; margin-bottom: 12px; font-size: 15px; letter-spacing: 0.6px; line-height: 1.35; }
  .contact-tab {
    width: 54px; height: 26px; background: var(--navy);
    display: flex; align-items: center; justify-content: flex-end; padding-right: 2px;
    margin-right: 16px; flex-shrink: 0;
  }
  .contact-icon {
    width: 22px; height: 22px; border-radius: 50%; background: var(--icon-bg);
    display: flex; align-items: center; justify-content: center;
  }
  .contact-icon svg { width: 12px; height: 12px; }
  .back-spine {
    position: absolute; left: 430px; top: 40px; width: 44px; height: 280px;
    border-radius: 22px;
    background: linear-gradient(180deg, transparent, var(--spine) 20%, var(--spine) 80%, transparent);
  }
  .back-brand {
    position: absolute; left: 330px; top: 148px; width: 230px;
    font-family: "Cormorant Garamond", serif; font-weight: 600;
    font-size: 27px; line-height: 1.05; color: var(--navy);
    display: flex; align-items: center; gap: 10px;
  }
  .back-brand .mark { width: 16px; height: 16px; background: var(--navy); border-radius: 50%; flex-shrink: 0; }
</style>
</head>
<body>

<section class="card card-front" aria-label="Card front">
  <div class="front-layout">
    <div class="front-spine" role="img" aria-label="Faint spine illustration"></div>
    <div class="front-brand"><span class="mark"></span>RV Spine &amp;<br>Vitality Center</div>
    <div class="slogan-pill">Steady Hands. Centered on You</div>
  </div>
</section>

<section class="card card-back" aria-label="Card back">
  <div class="back-spine" role="img" aria-label="Faint spine illustration"></div>
  <div class="name-block">
    <h1 class="doctor-name">LUCINDA FERROW, M.D.</h1>
    <p class="doctor-title">Board Certified Hand and Upper Extremity Surgeon</p>
  </div>
  <ul class="contact-list">
    <li class="contact-item">
      <span class="contact-tab"><span class="contact-icon">
        <svg viewBox="0 0 24 24" fill="none" stroke="#213f93" stroke-width="2"><path d="M5 3h4l2 5-3 2a11 11 0 0 0 6 6l2-3 5 2v4a2 2 0 0 1-2 2A17 17 0 0 1 3 5a2 2 0 0 1 2-2z"/></svg>
      </span></span>954-218-4630
    </li>
    <li class="contact-item">
      <span class="contact-tab"><span class="contact-icon">
        <svg viewBox="0 0 24 24" fill="#213f93"><rect x="6" y="3" width="12" height="6"/><rect x="3" y="10" width="18" height="8" rx="1"/><rect x="7" y="15" width="10" height="6" fill="#f3ecd6" stroke="#213f93" stroke-width="1.5"/></svg>
      </span></span>954-571-2846
    </li>
    <li class="contact-item">
      <span class="contact-tab"><span class="contact-icon">
        <svg viewBox="0 0 24 24" fill="none" stroke="#213f93" stroke-width="2"><rect x="3" y="5" width="18" height="14"/><path d="M3 5l9 8 9-8"/></svg>
      </span></span>info@myrvspine.example
    </li>
    <li class="contact-item">
      <span class="contact-tab"><span class="contact-icon">
        <svg viewBox="0 0 24 24" fill="#213f93"><path d="M12 2a7 7 0 0 0-7 7c0 5 7 13 7 13s7-8 7-13a7 7 0 0 0-7-7zm0 9.5A2.5 2.5 0 1 1 12 6.5a2.5 2.5 0 0 1 0 5z"/></svg>
      </span></span>38915 North Bramble Ave<br>Maple Ridge, FL 33482
    </li>
  </ul>
  <div class="back-brand"><span class="mark"></span><span>RV Spine &amp;<br>Vitality Center</span></div>
</section>

</body>
</html>
```